Business Card for Business consulting practice

Need a design for a consultant business card. Simple and elegant.
I need the following information on the card:
Logo: (see uploaded file)
Company name: Calmora Advisory Group
Name: Dana Weltrup
Title: Managing Director - Aerospace and Defence
Phone #: 514-268-3917
e-mail: dana.weltrup@calmora-example.com
Website: www.calmora-example.com
Tagline: Proposals Management and Capture support for complex procurements

```html
<!DOCTYPE html>
<html lang="en">
<head>
<meta charset="utf-8">
<title>Calmora Advisory Group – Business Card</title>
<link rel="stylesheet" href="https://fonts.googleapis.com/css2?family=Cinzel:wght@500;600&family=Arimo:wght@400&display=swap">
<style>
  :root {
    --backdrop: #1b1b1b;
    --kraft-light: #dfbf97;
    --kraft-mid: #c59d6f;
    --kraft-dark: #a3764a;
    --ink: #141210;
    --serif: "Cinzel", "Times New Roman", serif;
    --sans: "Arimo", Arial, sans-serif;
  }
  * { margin: 0; padding: 0; box-sizing: border-box; }
  html, body {
    width: 1093px; height: 1200px; overflow: hidden;
    background: var(--backdrop);
  }
  .canvas { position: relative; width: 1093px; height: 1200px; }
  .card {
    position: absolute; left: 264px; width: 580px; height: 357px;
    background: linear-gradient(135deg, var(--kraft-light) 0%, var(--kraft-mid) 50%, var(--kraft-dark) 100%);
    color: var(--ink); text-align: center;
  }
  .card--front { top: 226px; }
  .card--back { top: 620px; }

  .holder-name {
    position: absolute; top: 106px; left: 0; right: 0;
    font-family: var(--serif); font-weight: 600; font-size: 28px; letter-spacing: 0.5px;
    line-height: 1;
  }
  .holder-title {
    position: absolute; top: 138px; left: 0; right: 0;
    font-family: var(--sans); font-size: 18px; line-height: 1;
    word-spacing: 1px;
  }
  .divider-short {
    position: absolute; top: 168px; left: 236px; width: 107px; height: 1px;
    background: var(--ink);
  }
  .contact-list {
    position: absolute; top: 182px; left: 0; right: 0;
    list-style: none; font-family: var(--sans); font-size: 18px; line-height: 23.5px;
  }

  .brand {
    position: absolute; top: 128px; left: 0; right: 0;
    font-family: var(--serif); font-weight: 600;
  }
  .brand-name { display: block; font-size: 56px; line-height: 1; letter-spacing: 2px; }
  .brand-sub { display: block; margin-top: 8px; font-size: 16px; letter-spacing: 6px; }
  .divider-long {
    position: absolute; top: 275px; left: 107px; width: 368px; height: 1px;
    background: var(--ink);
  }
  .tagline {
    position: absolute; top: 287px; left: 0; right: 0;
    font-family: var(--sans); font-size: 17px; line-height: 21px; text-transform: uppercase;
  }
</style>
</head>
<body>
<main class="canvas">
  <section class="card card--front" aria-label="Card front">
    <h1 class="holder-name">DANA WELTRUP</h1>
    <p class="holder-title">Managing Director &nbsp;- &nbsp;Aerospace and Defence</p>
    <div class="divider-short"></div>
    <ul class="contact-list">
      <li>514-268-3917</li>
      <li>dana.weltrup@calmora-example.com</li>
      <li>www.calmora-example.com</li>
    </ul>
  </section>

  <section class="card card--back" aria-label="Card back">
    <div class="brand">
      <span class="brand-name">CALMORA</span>
      <span class="brand-sub">ADVISORY GROUP</span>
    </div>
    <div class="divider-long"></div>
    <p class="tagline">Proposals management and capture<br>support for complex procurements</p>
  </section>
</main>
</body>
</html>
```